Creating a website for a life changing company (Vantara Q)

We do need a website for our Coaching and Consulting business we recently launched. We do need it for information purposes and that our clients do have the opportunity to subscribe for packages, programs etc.
We would like to see designs which use the colours blue and yellow (see attachment). The final design should communicate our passion for the potential in people and the benefit (going beyond) for them.
Updates
Additional information:
Our company (webpage): Vantara Q (the C stands for "what people cannot see / imagine now...)
Welcome to Vantara Q(uest)
Consulting (O.R.B.) & Coaching (Rise onward)
Two pillars:
1) O.R.B. ( Leadership evolution - Our program - focussing on companies - business orientated)
2) Rise onward (Life transformation - Events - focusing on individuals - primarily life changing)
For both of them we offer: Concierge & Vantara Q+ (This should go as a subscription)
Eventually you can draft this as a rhombus
Industry/Entity Type
Coaching / Consulting
Coding
Coded - Design and coding required
Number of Pages Required
1 page
Font styles to use
Other font styles liked:
- Lato
Requirements
Must have
- Please see attachment (About us / Offers / Calendar function / Links to Instagram and LinkedIn account / mailing list / page for clients
Nice to have
- A banner

```html
<!DOCTYPE html>
<html lang="en">
<head>
<meta charset="utf-8">
<title>Vantara Q – Coaching &amp; Consulting</title>
<link href="https://fonts.googleapis.com/css2?family=Lato:ital,wght@0,400;0,700;1,400&family=Montserrat:wght@400;600;700;800&display=swap" rel="stylesheet">
<style>
:root{
  --blue:#0d4a9e;
  --blue-dark:#0a3673;
  --navy:#12264d;
  --yellow:#ffc20e;
  --yellow-soft:#ffd54a;
  --text:#5b6575;
  --muted:#8a93a3;
  --line:#e2e7ef;
  --pale:#eef3f8;
  --white:#ffffff;
}
*{box-sizing:border-box;margin:0;padding:0}
html,body{width:1200px;height:5372px;overflow:hidden}
body{position:relative;font-family:"Lato",sans-serif;color:var(--text);background:var(--white)}
.abs{position:absolute}
.heading{font-family:"Montserrat",sans-serif;font-weight:700;color:var(--navy)}
.hl{color:var(--yellow)}
a{color:inherit;text-decoration:none}

.topbar{top:0;left:0;width:1200px;height:42px;font-size:10px;color:var(--muted);letter-spacing:.3px}
.topbar .item{top:14px;display:flex;align-items:center;gap:8px}
.logo{display:flex;align-items:center;gap:10px}
.logo .dot{width:22px;height:22px;border-radius:50%;background:var(--yellow)}
.logo .name{font-family:"Lato",sans-serif;font-weight:700;font-size:20px;letter-spacing:3px;color:var(--blue)}
.contact{display:flex;align-items:center;gap:14px;font-size:11px;line-height:19px;color:var(--text)}
.nav{top:167px;left:0;width:1200px;height:43px}
.nav a{position:absolute;top:14px;font-family:"Montserrat",sans-serif;font-weight:700;font-size:11px;color:var(--navy)}

.hero{top:219px;left:0;width:1200px;height:778px;background:linear-gradient(160deg,#c9d3df 0%,#eef1f5 35%,#dfe4ea 60%,#aeb8c4 100%)}
.hero-box{top:432px;left:71px;width:545px;height:278px;background:rgba(13,74,158,.94);padding:38px 52px;color:var(--white)}
.hero-box h1{font-family:"Montserrat",sans-serif;font-size:25px;line-height:32px;font-weight:700;color:var(--white)}
.hero-box p{margin-top:14px;font-size:14.5px;line-height:23px}
.btn{display:inline-flex;align-items:center;justify-content:center;font-family:"Montserrat",sans-serif;font-size:11px;font-weight:600;letter-spacing:.5px}
.btn-yellow{background:var(--yellow);color:var(--white)}
.btn-blue{background:var(--blue);color:var(--white)}

.pale-band{top:997px;left:0;width:1200px;height:740px;background:var(--pale)}
.cred{top:941px;left:110px;width:975px;height:670px;background:var(--white);box-shadow:0 10px 30px rgba(18,38,77,.08);overflow:hidden}
.cred-photo{top:0;left:650px;width:325px;height:670px;background:linear-gradient(100deg,rgba(255,255,255,1) 0%,#f3f1ea 30%,#f6d35a 60%,#e7ad12 85%,#b7c2cf 100%)}
.cred h2{top:80px;left:53px;font-size:25px}
.cred .lead{top:128px;left:53px;width:520px;font-style:italic;font-size:13.5px;line-height:22px}
.feat{width:280px}
.feat svg{display:block}
.feat h3{margin-top:20px;font-family:"Montserrat",sans-serif;font-size:13.5px;font-weight:700;color:var(--navy)}
.feat p{margin-top:14px;font-size:13px;line-height:23px}

.scroll-down{top:1704px;left:567px;width:60px;height:60px;border-radius:50%;background:var(--yellow);display:flex;align-items:center;justify-content:center}

.sec-title{left:0;width:1200px;text-align:center;font-size:48px;font-weight:800}
.sec-sub{left:0;width:1200px;text-align:center;font-size:14.5px;line-height:25px}

.card{width:217px;background:var(--white);border:1px solid var(--line);text-align:center;padding:0 22px}
.card .icon{position:absolute;top:-29px;left:79px;width:58px;height:58px;border-radius:50%;background:var(--blue);display:flex;align-items:center;justify-content:center}
.card h3{margin-top:74px;font-family:"Montserrat",sans-serif;font-size:13px;font-weight:700;color:var(--navy);line-height:17px}
.card p{margin-top:14px;font-size:13px;line-height:23px}
.card .more{margin-top:22px;display:flex;justify-content:center;gap:12px;font-family:"Montserrat",sans-serif;font-size:11px;font-weight:700;color:var(--blue)}
.promo{top:2402px;left:855px;width:217px;height:253px;background:linear-gradient(180deg,#5e86c5 0%,#9db8de 45%,#7b6b5d 100%)}
.promo .tag{top:78px;left:18px;background:var(--yellow);color:var(--white);font-size:10px;padding:4px 10px;font-weight:700}
.promo .bar{bottom:0;left:0;width:217px;height:42px;background:rgba(13,74,158,.92);color:var(--white);font-size:10px;display:flex;align-items:center;justify-content:center}
.promo .mark{top:24px;left:0;width:217px;display:flex;justify-content:center}

.plan{top:2805px;left:0;width:1200px;height:446px;background:linear-gradient(180deg,#16284c 0%,#213b68 55%,#2d4f85 100%)}
.plan h2{top:160px;left:0;width:1200px;text-align:center;font-family:"Montserrat",sans-serif;font-size:28px;font-weight:700;color:var(--white)}
.plan p{top:224px;left:0;width:1200px;text-align:center;font-size:13.5px;line-height:24px;color:var(--white)}
.diamond{width:148px;height:148px;transform:rotate(45deg);border:7px solid var(--white);box-shadow:0 8px 20px rgba(0,0,0,.15)}
.step{width:300px;text-align:center}
.step h3{font-family:"Montserrat",sans-serif;font-size:13.5px;font-weight:600;letter-spacing:1px;color:var(--navy)}
.step p{margin-top:22px;font-size:13px;line-height:23px}

.split-left{top:3562px;left:0;width:597px;height:378px;background:linear-gradient(135deg,#1d4f96 0%,#2a62ad 50%,#12407f 100%)}
.split-right{top:3562px;left:597px;width:603px;height:378px;background:linear-gradient(135deg,#ffce2e 0%,#f6c21a 55%,#e8b00c 100%)}
.split-in{position:absolute;top:0;left:0;width:100%;height:100%;text-align:center;padding-top:103px}
.split-in h2{font-family:"Montserrat",sans-serif;font-size:28px;font-weight:700}
.split-in p{margin:20px auto 0;width:500px;font-size:13.5px;line-height:24px}
.split-in .btn{margin-top:36px;width:154px;height:38px}

.member{width:217px;height:311px}
.member .photo{width:217px;height:244px}
.member .plate{width:217px;height:67px;background:var(--blue);text-align:center;padding-top:18px}
.member .plate b{display:block;font-family:"Montserrat",sans-serif;font-size:14px;color:var(--white)}
.member .plate i{display:block;margin-top:4px;font-family:"Montserrat",sans-serif;font-size:10px;font-weight:600;color:var(--yellow)}

.cta{top:4664px;left:0;width:1200px;height:174px;background:var(--yellow)}
.cta .small{top:56px;left:123px;font-family:"Montserrat",sans-serif;font-size:27px;font-weight:400;color:var(--navy)}
.cta .big{top:92px;left:123px;font-family:"Montserrat",sans-serif;font-size:25px;font-weight:700;color:var(--navy)}
.cta .outline{top:49px;left:817px;width:211px;height:46px;border:2px solid var(--blue);color:var(--blue);font-size:12px}

.footer{top:4838px;left:0;width:1200px;height:498px;background:linear-gradient(180deg,#0d4fa8 0%,#0b3f88 100%);color:#dbe5f5;font-size:12.5px}
.footer h4{position:absolute;top:88px;font-family:"Montserrat",sans-serif;font-size:17px;font-weight:700;color:var(--white);border-left:3px solid var(--yellow);padding-left:14px;line-height:22px}
.footer .links a{display:block;font-size:12.5px;line-height:32px}
.finfo{display:flex;gap:14px;line-height:20px}
.field{border-bottom:2px solid var(--yellow);font-size:10px;color:#c7d5ec;padding-bottom:12px;width:217px}
.social{display:flex;gap:28px}
.social span{width:18px;height:18px;border-radius:50%;background:var(--white)}
.bottom{top:5336px;left:0;width:1200px;height:36px;background:#0a3572;color:#c7d5ec;font-size:10px}
.bottom .nav2{position:absolute;top:12px;right:120px;display:flex;gap:26px}
</style>
</head>
<body>

<div class="abs topbar">
  <div class="abs item" style="left:130px">
    <svg width="14" height="10" viewBox="0 0 14 10"><rect x=".5" y=".5" width="13" height="9" fill="none" stroke="#ffc20e"/><path d="M.5 .5 7 6 13.5 .5" fill="none" stroke="#ffc20e"/></svg>
    INFO@VANTARA-Q.COM
  </div>
  <div class="abs item" style="left:862px">
    <svg width="13" height="13" viewBox="0 0 14 14"><circle cx="7" cy="7" r="6" fill="none" stroke="#ffc20e" stroke-width="1.4"/><path d="M7 3.5V7l2.5 1.5" fill="none" stroke="#ffc20e" stroke-width="1.4"/></svg>
    MONDAY – FRIDAY : 8:00 AM TO 5:00 PM
  </div>
</div>

<header>
  <div class="abs logo" style="top:84px;left:170px">
    <span class="dot"></span><span class="name">VANTARA Q</span>
  </div>
  <div class="abs contact" style="top:82px;left:695px">
    <svg width="16" height="22" viewBox="0 0 16 22"><path d="M8 1a7 7 0 0 0-7 7c0 5 7 13 7 13s7-8 7-13a7 7 0 0 0-7-7z" fill="none" stroke="#ffc20e" stroke-width="1.6"/><circle cx="8" cy="8" r="2.5" fill="#ffc20e"/></svg>
    <div>48 Lindenhall Road<br>Brookfield, MD 20900</div>
  </div>
  <div class="abs contact" style="top:82px;left:922px">
    <svg width="20" height="20" viewBox="0 0 20 20"><path d="M4 1l4 4-2 3c1 3 3 5 6 6l3-2 4 4-3 3C9 19 1 11 1 4z" fill="none" stroke="#ffc20e" stroke-width="1.6" stroke-linejoin="round"/></svg>
    <div>+1(10) 555 014 2281<br>+1(10) 555 014 2292</div>
  </div>
  <nav class="abs nav">
    <a href="#" style="left:150px">VANTARA Q</a>
    <a href="#" style="left:265px">ABOUT US</a>
    <a href="#" style="left:382px">O.R.B.</a>
    <a href="#" style="left:463px">CONCIERGE</a>
    <a href="#" style="left:590px">RISE ONWARD</a>
    <a href="#" style="left:716px">VANTARA Q+</a>
    <a href="#" style="left:839px">TESTIMONIALS</a>
  </nav>
</header>

<section class="abs hero" role="img" aria-label="Photo of a business team meeting around a conference table while a presenter points to a sales chart on a screen"></section>
<div class="abs hero-box">
  <h1>CREATING A <span class="hl">LANDMARK</span><br>TO BE REMEMBERED</h1>
  <p>They’ll have to make the best of things its an uphill climb. The weather started getting rough the tiny ship was tossed. If not for the courage of the fearless.</p>
  <a href="#" class="btn btn-yellow" style="margin-top:24px;width:125px;height:38px">KNOW MORE</a>
</div>

<div class="abs pale-band"></div>
<section class="abs cred">
  <div class="abs cred-photo" role="img" aria-label="Photo of a worker in a tool belt holding a yellow hard hat in a gloved hand"></div>
  <h2 class="abs heading">CHECK OUT <span class="hl">OUR CREDENTIALS</span></h2>
  <p class="abs lead">Straight ahead and on the track now. We’re gonna make our dreams come true, black gold Doin’ it our way.</p>

  <div class="abs feat" style="top:224px;left:53px">
    <svg width="44" height="48" viewBox="0 0 44 48"><path d="M6 42 30 18l6 6-24 24z" fill="#0d4a9e"/><path d="M30 4l10 10-6 6-10-10z" fill="#0d4a9e"/></svg>
    <h3>CONTEMPORARY DESIGN</h3>
    <p>Could you be mine. And when the odds are against him and their dangers work to do. You can count on us every step.</p>
  </div>
  <div class="abs feat" style="top:224px;left:364px">
    <svg width="44" height="48" viewBox="0 0 44 48"><path d="M4 46V24l10-6v6l10-6v6l10-6V6h6v40z" fill="#0d4a9e"/><rect x="32" y="2" width="10" height="4" fill="#0d4a9e"/></svg>
    <h3>INNOVATIVE APPROACH</h3>
    <p>Could you be mine. And when the odds are against him and their dangers work to do. You can count on us every step.</p>
  </div>
  <div class="abs feat" style="top:430px;left:53px">
    <svg width="44" height="44" viewBox="0 0 44 44"><rect x="4" y="22" width="28" height="12" fill="#0d4a9e"/><rect x="4" y="36" width="36" height="6" rx="3" fill="#0d4a9e"/><path d="M8 22V8l18 8" fill="none" stroke="#0d4a9e" stroke-width="4"/></svg>
    <h3>URBAN LIVING AT ITS BEST</h3>
    <p>Could you be mine. And when the odds are against him and their dangers work to do. You can count on us every step.</p>
  </div>
  <div class="abs feat" style="top:430px;left:364px">
    <svg width="44" height="44" viewBox="0 0 44 44"><circle cx="16" cy="8" r="6" fill="#0d4a9e"/><path d="M8 42V20h16v22h-5V30h-6v12z" fill="#0d4a9e"/><rect x="28" y="30" width="10" height="12" fill="#0d4a9e"/></svg>
    <h3>THE TEAM WORK</h3>
    <p>Could you be mine. And when the odds are against him and their dangers work to do. You can count on us every step.</p>
  </div>
</section>

<div class="abs scroll-down">
  <svg width="22" height="22" viewBox="0 0 22 22"><circle cx="11" cy="11" r="10" fill="#12264d"/><path d="M11 6v9M7 11l4 4 4-4" fill="none" stroke="#ffc20e" stroke-width="2"/></svg>
</div>

<h2 class="abs heading sec-title" style="top:1848px">Peace of <span class="hl">Mind</span></h2>
<p class="abs sec-sub" style="top:1928px">Sometimes you want to go where everybody knows your name. And they’re always glad you came. Straight nin’ the curves<br>flatnin’ the hills Someday the mountain will.</p>

<div class="abs card" style="top:2055px;left:123px;height:300px">
  <div class="icon"><svg width="26" height="26" viewBox="0 0 26 26"><path d="M3 22h20M5 22V12l8-7 8 7v10" fill="none" stroke="#fff" stroke-width="2"/></svg></div>
  <h3>OUR EXPERIENCE<br>SPEAKS</h3>
  <p>Doin’ it our way. Nothin’s gonna turn us back now. Straight ahead and on the track now.</p>
  <div class="more">READ MORE <span class="hl">→</span></div>
</div>
<div class="abs card" style="top:2055px;left:367px;height:300px">
  <div class="icon"><svg width="26" height="26" viewBox="0 0 26 26"><circle cx="13" cy="9" r="5" fill="#fff"/><path d="M4 24c0-6 4-9 9-9s9 3 9 9z" fill="#fff"/></svg></div>
  <h3>COMPETENT STAFF</h3>
  <p>Doin’ it our way. Nothin’s gonna turn us back now. Straight ahead and on the track now.</p>
  <div class="more">READ MORE <span class="hl">→</span></div>
</div>
<div class="abs card" style="top:2055px;left:611px;height:300px">
  <div class="icon"><svg width="26" height="26" viewBox="0 0 26 26"><path d="M13 3v20M6 8h14M8 23h10" fill="none" stroke="#fff" stroke-width="2"/></svg></div>
  <h3>DEPLOYING<br>TECHNOLOGY</h3>
  <p>Doin’ it our way. Nothin’s gonna turn us back now. Straight ahead and on the track now.</p>
  <div class="more">READ MORE <span class="hl">→</span></div>
</div>
<div class="abs card" style="top:2055px;left:855px;height:283px">
  <div class="icon"><svg width="26" height="26" viewBox="0 0 26 26"><path d="M4 22 16 10M14 4l8 8-4 4-8-8z" fill="none" stroke="#fff" stroke-width="2"/></svg></div>
  <h3>EXPERTS AT WORK</h3>
  <p>Doin’ it our way. Nothin’s gonna turn us back now. Straight ahead and on the track now.</p>
  <div class="more">READ MORE <span class="hl">→</span></div>
</div>

<div class="abs card" style="top:2414px;left:123px;height:283px">
  <div class="icon"><svg width="26" height="26" viewBox="0 0 26 26"><rect x="5" y="5" width="16" height="16" fill="none" stroke="#fff" stroke-width="2"/><path d="M9 13l3 3 5-6" fill="none" stroke="#fff" stroke-width="2"/></svg></div>
  <h3>BEST MATERIALS</h3>
  <p>Doin’ it our way. Nothin’s gonna turn us back now. Straight ahead and on the track now.</p>
  <div class="more">READ MORE <span class="hl">→</span></div>
</div>
<div class="abs card" style="top:2414px;left:367px;height:300px">
  <div class="icon"><svg width="26" height="26" viewBox="0 0 26 26"><circle cx="13" cy="13" r="9" fill="none" stroke="#fff" stroke-width="2"/><path d="M9 13l3 3 5-6" fill="none" stroke="#fff" stroke-width="2"/></svg></div>
  <h3>QUALITY AT EVERY<br>STEP</h3>
  <p>Doin’ it our way. Nothin’s gonna turn us back now. Straight ahead and on the track now.</p>
  <div class="more">READ MORE <span class="hl">→</span></div>
</div>
<div class="abs card" style="top:2414px;left:611px;height:283px">
  <div class="icon"><svg width="26" height="26" viewBox="0 0 26 26"><path d="M5 5l16 16M21 5 5 21" fill="none" stroke="#fff" stroke-width="2"/></svg></div>
  <h3>COMPETITIVE PRICE</h3>
  <p>Doin’ it our way. Nothin’s gonna turn us back now. Straight ahead and on the track now.</p>
  <div class="more">READ MORE <span class="hl">→</span></div>
</div>
<div class="abs promo" role="img" aria-label="Photo of modern apartment buildings under a blue sky">
  <div class="abs mark"><div class="logo"><span class="dot" style="width:12px;height:12px"></span><span class="name" style="font-size:10px;color:#fff">VANTARA Q</span></div></div>
  <div class="abs tag">Explore Projects</div>
  <div class="abs bar">Get Quote or Call Us for Details</div>
</div>

<section class="abs plan" role="img" aria-label="Photo of high-rise buildings under construction at dusk">
  <h2 class="abs">PLAN THE WORK - <span class="hl">WORK THE PLAN</span></h2>
  <p class="abs">Sometimes you want to go where everybody knows your name. And they’re always glad you came.<br>Straight nin’ the curves flatnin’ the hills Someday the mountain will.</p>
</section>
<div class="abs diamond" style="top:3171px;left:204px;background:linear-gradient(135deg,#7ea9d8,#f0c23a 60%,#e9eef5)" role="img" aria-label="Photo of two engineers in hard hats reviewing plans"></div>
<div class="abs diamond" style="top:3171px;left:523px;background:linear-gradient(135deg,#f4f6f9,#cfd8e3 55%,#eef2f6)" role="img" aria-label="Photo of hands working over architectural drawings with glasses"></div>
<div class="abs diamond" style="top:3171px;left:846px;background:linear-gradient(135deg,#c9d4e0,#e8a93a 55%,#6c7f96)" role="img" aria-label="Photo of builders in hard hats assembling a structure"></div>

<div class="abs step" style="top:3386px;left:128px"><h3>OUR TEAM OF ENGINEERS</h3><p>Could you be mine. And when the odds are against him and their dangers work to do. You can count on us every step.</p></div>
<div class="abs step" style="top:3386px;left:447px"><h3>METICULOUS PLANNING</h3><p>Could you be mine. And when the odds are against him and their dangers work to do. You can count on us every step.</p></div>
<div class="abs step" style="top:3386px;left:770px"><h3>SYSTEMATIC IMPLEMENTATION</h3><p>Could you be mine. And when the odds are against him and their dangers work to do. You can count on us every step.</p></div>

<section class="abs split-left" role="img" aria-label="Photo of a professional at work, tinted blue">
  <div class="split-in" style="color:#fff">
    <h2>O.R.B. <span class="hl">PROJECTS</span></h2>
    <p>Straight ahead and on the track now. We’re gonna make our dreams come true, black gold Doin’ it our way.</p>
    <a href="#" class="btn btn-yellow">GET A QUOTE</a>
  </div>
</section>
<section class="abs split-right" role="img" aria-label="Photo of a professional at work, tinted yellow">
  <div class="split-in" style="color:#fff">
    <h2><span style="color:var(--blue)">VANTARA Q</span> PROJECTS</h2>
    <p>Straight ahead and on the track now. We’re gonna make our dreams come true, black gold Doin’ it our way.</p>
    <a href="#" class="btn btn-blue">GET A QUOTE</a>
  </div>
</section>

<h2 class="abs heading sec-title" style="top:4034px">Our Great <span class="hl">Team</span></h2>
<p class="abs sec-sub" style="top:4115px;font-size:13px;line-height:24px">Sometimes you want to go where everybody knows your name. And they’re always glad you came. Straight nin’ the curves<br>flatnin’ the hills Someday the mountain will.</p>

<div class="abs member" style="top:4218px;left:123px">
  <div class="photo" role="img" aria-label="Portrait photo of co-founder Lukas Brennan in a navy suit" style="background:linear-gradient(180deg,#4a6f9e,#2b4670)"></div>
  <div class="plate"><b>LUKAS BRENNAN</b><i>CO FOUNDER</i></div>
</div>
<div class="abs member" style="top:4218px;left:367px">
  <div class="photo" role="img" aria-label="Portrait photo of co-founder Mira Castell in a yellow jacket" style="background:linear-gradient(180deg,#e6e8ea,#f0c030)"></div>
  <div class="plate"><b>MIRA CASTELL</b><i>CO FOUNDER</i></div>
</div>
<div class="abs member" style="top:4218px;left:611px">
  <div class="photo" role="img" aria-label="Portrait photo of Owen Harlow in a dark suit" style="background:linear-gradient(180deg,#f2f3f5,#27344a)"></div>
  <div class="plate"><b>OWEN HARLOW</b><i>DESIGNATION</i></div>
</div>
<div class="abs member" style="top:4218px;left:855px">
  <div class="photo" role="img" aria-label="Portrait photo of Elena Voss holding a teal umbrella" style="background:linear-gradient(180deg,#3f93a6,#d9dde2 60%,#213a5e)"></div>
  <div class="plate"><b>ELENA VOSS</b><i>DESIGNATION</i></div>
</div>

<section class="abs cta">
  <svg class="abs" style="top:0;left:0" width="1200" height="174" viewBox="0 0 1200 174"><polygon points="725,0 1200,0 1200,174 725,174 760,87" fill="#ffd23d"/></svg>
  <div class="abs small">Have any ideas in your mind?</div>
  <div class="abs big">CREATE YOUR NEXT PROJECT WITH US</div>
  <a href="#" class="abs btn outline">REQUEST A QUOTE</a>
</section>

<footer class="abs footer">
  <div class="abs logo" style="top:112px;left:150px">
    <span class="dot" style="background:var(--yellow)"></span><span class="name" style="color:#fff">VANTARA Q</span>
  </div>
  <p class="abs" style="top:222px;left:123px;width:215px;line-height:23px">Our projects spell success because success is a project that is always under construction. We build and deliver your vision exactly every time!</p>
  <div class="abs social" style="top:342px;left:130px" aria-label="Social media links">
    <span></span><span></span><span></span><span></span>
  </div>

  <h4 style="left:395px">QUICK LINKS</h4>
  <div class="abs links" style="top:136px;left:395px">
    <a href="#">Vantara Q</a><a href="#">O.R.B.</a><a href="#">Concierge</a><a href="#">Rise onward</a><a href="#">Vantara Q+</a><a href="#">Testimonials</a>
  </div>

  <h4 style="left:610px">GET IN TOUCH</h4>
  <div class="abs finfo" style="top:146px;left:610px">
    <svg width="14" height="18" viewBox="0 0 16 22"><path d="M8 1a7 7 0 0 0-7 7c0 5 7 13 7 13s7-8 7-13a7 7 0 0 0-7-7z" fill="none" stroke="#ffc20e" stroke-width="2"/></svg>
    <div>2190 Harbor Crest Ave.<br>Fairview, NJ 07100</div>
  </div>
  <div class="abs finfo" style="top:226px;left:610px">
    <svg width="16" height="16" viewBox="0 0 20 20"><path d="M4 1l4 4-2 3c1 3 3 5 6 6l3-2 4 4-3 3C9 19 1 11 1 4z" fill="none" stroke="#ffc20e" stroke-width="2" stroke-linejoin="round"/></svg>
    <div>+(01) 555 019 3304<br>+(01) 555 019 3315</div>
  </div>
  <div class="abs finfo" style="top:296px;left:610px">
    <svg width="16" height="12" viewBox="0 0 14 10"><rect x=".5" y=".5" width="13" height="9" fill="none" stroke="#ffc20e"/><path d="M.5 .5 7 6 13.5 .5" fill="none" stroke="#ffc20e"/></svg>
    <div>info@vantara-q.com<br>support@vantara-q.com</div>
  </div>

  <h4 style="left:855px">DROP A MESSAGE</h4>
  <div class="abs field" style="top:152px;left:855px">NAME</div>
  <div class="abs field" style="top:205px;left:855px">EMAIL</div>
  <div class="abs field" style="top:258px;left:855px;height:90px">YOUR MESSAGE</div>
  <a href="#" class="abs btn btn-yellow" style="top:370px;left:855px;width:217px;height:40px;color:var(--blue)">SEND NOW</a>
</footer>
<div class="abs bottom">
  <div class="abs" style="top:12px;left:123px">COPYRIGHT © 2022 VANTARA Q. ALL RIGHTS RESERVED.</div>
  <div class="nav2"><span>HOME</span><span>SERVICES</span><span>TERMS &amp; CONDITION</span><span>PRIVACY POLICY</span><span>CONTACT US</span></div>
  <svg class="abs" style="top:-30px;left:1128px" width="60" height="60" viewBox="0 0 60 60"><rect x="14" y="14" width="32" height="32" transform="rotate(45 30 30)" fill="#0a3572" stroke="#7f9cc8"/><path d="M30 38V22M24 28l6-6 6 6" fill="none" stroke="#c7d5ec" stroke-width="1.5"/></svg>
</div>

</body>
</html>
```